seeking a modern Business Card design for Roof Plumbering Business

wexcombe roof plumbing is a local metal re-roof and new construction specialist. We are seeking a modern business card to assist with networking within the industry. Our services are predominantly the installation of metal roofs on new houses, however we also do re-roofs when an existing roof needs replacing. We service both residential and commercial properties. Please include the below details on the card:
Name: Owen Wexcombe
Phone: 0471 385 962
Email: owenwexcomberoofing@mailnest.example

Residential & Commercial
Re-roof & New Construction
Fully Insured

I have uploaded our business logo, which we think would suit a black background. Please use all lower case for business name.
Cheers
Updates

Hey Guys, As requested I've uploaded a Pdf version of my logo. Hopefully this help. Thanks

Industry/Entity Type

Business

Contact Information for Business Card

Name: Owen Wexcombe
Phone: 0471 385 962

Residential & Commercial
Fully Insured

Font styles to use
Serif
Sans Serif

Requirements
Must have
• Name must be all lower case "wexcombe roof plumbing"
Nice to have
• Stick with Logo Colours

```html
<!DOCTYPE html>
<html lang="en">
<head>
<meta charset="utf-8">
<title>wexcombe roof plumbing – business card</title>
<link href="https://fonts.googleapis.com/css2?family=Open+Sans:wght@400;600;700&display=swap" rel="stylesheet">
<style>
  :root {
    --sky: #24bde8;
    --ink: #060606;
    --paper: #ffffff;
    --stage: #e9e6e1;
    --muted: #f2f2f2;
  }
  * { box-sizing: border-box; margin: 0; padding: 0; }
  html, body {
    width: 1200px; height: 900px; overflow: hidden;
    background: var(--stage);
    font-family: "Open Sans", Arial, sans-serif;
  }
  .canvas { position: relative; width: 1200px; height: 900px; }

  .card {
    position: absolute;
    width: 580px; height: 332px;
    box-shadow: 0 6px 18px rgba(0,0,0,.18);
  }
  .card--front { left: 90px; top: 100px; background: var(--sky); color: var(--paper); }
  .card--back  { left: 530px; top: 420px; background: var(--ink); color: var(--sky); }

  /* services list */
  .services {
    position: absolute; left: 300px; top: 40px;
    list-style: none; font-weight: 600; font-size: 15px; line-height: 24px;
  }
  .services li { display: flex; align-items: center; gap: 9px; }
  .services li:nth-child(2) { padding-left: 10px; }
  .services li:nth-child(3) { padding-left: 20px; }
  .services svg { width: 9px; height: 9px; flex: none; }

  /* wordmark stand-in */
  .wordmark {
    position: absolute; left: 40px; bottom: 52px;
    display: flex; align-items: center; gap: 12px;
    font-weight: 600; font-size: 30px; letter-spacing: .5px;
  }
  .wordmark__square { width: 18px; height: 18px; background: currentColor; flex: none; }
  .card--front .wordmark { color: var(--paper); }
  .card--back  .wordmark { color: var(--sky); bottom: 60px; }

  /* contact block */
  .contact { position: absolute; left: 290px; top: 44px; }
  .contact__name { font-weight: 600; font-size: 19px; margin-bottom: 16px; }
  .contact__line {
    display: flex; align-items: center; gap: 10px;
    color: var(--muted); font-size: 13px; line-height: 22px;
  }
  .contact__line svg { width: 12px; height: 12px; flex: none; }
</style>
</head>
<body>
<main class="canvas">

  <section class="card card--front" aria-label="Card front">
    <ul class="services">
      <li><svg viewBox="0 0 10 10"><path d="M5 0 10 5 5 10 0 5Z" fill="currentColor"/></svg>Residential &amp; Commercial</li>
      <li><svg viewBox="0 0 10 10"><path d="M5 0 10 5 5 10 0 5Z" fill="currentColor"/></svg>Re-roof &amp; New Construction</li>
      <li><svg viewBox="0 0 10 10"><path d="M5 0 10 5 5 10 0 5Z" fill="currentColor"/></svg>Fully Insured</li>
    </ul>
    <div class="wordmark"><span class="wordmark__square"></span>wexcombe roof plumbing</div>
  </section>

  <section class="card card--back" aria-label="Card back">
    <div class="contact">
      <p class="contact__name">Owen Wexcombe</p>
      <p class="contact__line">
        <svg viewBox="0 0 24 24"><path fill="var(--sky)" d="M6.6 10.8a15 15 0 0 0 6.6 6.6l2.2-2.2a1 1 0 0 1 1-.25 11.4 11.4 0 0 0 3.6.57 1 1 0 0 1 1 1V20a1 1 0 0 1-1 1A17 17 0 0 1 3 4a1 1 0 0 1 1-1h3.5a1 1 0 0 1 1 1c0 1.25.2 2.45.57 3.57a1 1 0 0 1-.25 1z"/></svg>
        0471 385 962
      </p>
      <p class="contact__line">
        <svg viewBox="0 0 24 24"><rect x="2" y="5" width="20" height="14" rx="1.5" fill="var(--sky)"/><path d="M3 6.5 12 13l9-6.5" fill="none" stroke="var(--ink)" stroke-width="1.6"/></svg>
        owenwexcomberoofing@mailnest.example
      </p>
    </div>
    <div class="wordmark"><span class="wordmark__square"></span>wexcombe roof plumbing</div>
  </section>

</main>
</body>
</html>
```